Real Estate Sign - For Sale Yard Sign - Bellwether Estates

Our real estate company is looking for a new sign design to hang from in post in the front yard of the homes we are selling. Our company name is Bellwether Estates and we are open to any ideas. Attached for you is our company logo and name. The font is Trajan Pro. We are looking for a classy sign to put in front of our high end more expensive homes. You can either choose to include or not include the words "FOR SALE" on the sign (in our state, only about 1/2 of the real estate signs have room for those words. It is implied with a sign in the yard in front of a home). Thank you.

24 inches wide is important. and the height should be either 18, 24 or 30 inches. For printing purposes either of those heights will work. 18 inches is common, but some signs look great that are taller too. I'm open.

If you have any ideas for some better text options, styles or fonts, feel free to play with it.

P.S. Please feel free to play with the colors. We are not at this point set on a particular color scheme. Colors we think are nice but you may have other better ideas are black, red, white, gold, green

Target Market(s)

High end real estate home owners who choose to use our company to sell their home.

Industry/Entity Type

Real Estate

Requirements
Must have
• Company Logo
Company Name (Bellwether Estates)
Thaddeus Vornholt (please include my name as I am the real estate agent)
503-618-2940 (my phone number for potential clients to contact me)
Website name - bellwetherestatesnw.example
***You can either choose to include the words "FOR SALE" or not***

Dimensions must be 24 inches wide. Height can be either 18, 24 or 30 inches. Must be one of those 3 heights for printing purposes.

```html
<!DOCTYPE html>
<html lang="en">
<head>
<meta charset="utf-8">
<title>Bellwether Estates – Yard Sign</title>
<link rel="stylesheet" href="https://fonts.googleapis.com/css2?family=Cinzel:wght@400;600;700&display=swap">
<style>
  :root {
    --page: #ffffff;
    --sign-red: #c10618;
    --cream: #f9f8ef;
    --brown-dark: #4f4630;
    --band-light: #7d725b;
    --band-dark: #59513c;
    --gold: #d8c9a0;
    --white: #ffffff;
  }
  * { margin: 0; padding: 0; box-sizing: border-box; }
  html, body {
    width: 1200px; height: 799px; overflow: hidden;
    background: var(--page);
    font-family: "Cinzel", "Trajan Pro", serif;
  }
  .canvas { position: relative; width: 1200px; height: 799px; }
  .yard-sign {
    position: absolute; left: 373px; top: 150px;
    width: 414px; height: 519px;
  }
  .sign-frame { position: absolute; inset: 0; }
  .brand-mark {
    position: absolute; left: 177px; top: 68px;
    width: 60px; height: 60px; border-radius: 50%;
    background: var(--gold);
  }
  .brand-name {
    position: absolute; left: 10px; right: 10px;
    text-align: center; color: var(--brown-dark); font-weight: 600;
    line-height: 1;
  }
  .brand-name--primary { top: 150px; font-size: 44px; letter-spacing: 1px; }
  .brand-name--secondary { top: 200px; font-size: 28px; letter-spacing: 3px; }
  .agent-band {
    position: absolute; left: 10px; right: 10px;
    display: flex; align-items: center; justify-content: center;
    color: var(--white); font-weight: 600;
  }
  .agent-band--name {
    top: 291px; height: 73px; background: var(--band-light);
    font-size: 30px; letter-spacing: 1px;
    font-variant: small-caps; text-transform: none;
  }
  .agent-band--phone {
    top: 365px; height: 74px; background: var(--band-dark);
    font-size: 40px; letter-spacing: 3px;
  }
  .website {
    position: absolute; left: 10px; right: 10px; top: 462px;
    text-align: center; color: var(--brown-dark);
    font-size: 15px; font-weight: 700; letter-spacing: 0.5px;
    text-transform: uppercase;
  }
</style>
</head>
<body>
  <main class="canvas">
    <section class="yard-sign" aria-label="Bellwether Estates for sale sign">
      <svg class="sign-frame" width="414" height="519" viewBox="0 0 414 519" aria-hidden="true">
        <rect width="414" height="519" fill="var(--sign-red)"/>
        <polygon points="207,12 404,84 404,509 10,509 10,84" fill="var(--cream)"/>
      </svg>
      <span class="brand-mark" aria-hidden="true"></span>
      <div class="brand-name brand-name--primary">BELLWETHER</div>
      <div class="brand-name brand-name--secondary">ESTATES</div>
      <div class="agent-band agent-band--name">Thaddeus Vornholt</div>
      <div class="agent-band agent-band--phone">503-618-2940</div>
      <div class="website">bellwetherestatesnw.example</div>
    </section>
  </main>
</body>
</html>
```